Medical Company in need of Modern business card design for new Wound Care clinic.

Modern business card design for our Woundcare company. Logo and description of services can be found on our website; https://www.tornvel-skinheal.com/

```html
<!DOCTYPE html>
<html lang="en">
<head>
<meta charset="utf-8">
<title>Tornvel Skinheal – Business Card</title>
<link href="https://fonts.googleapis.com/css2?family=Lato:wght@400;700&display=swap" rel="stylesheet">
<style>
  :root {
    --page-bg: #2b2b2d;
    --gold-light: #e2b567;
    --gold-mid: #cc9a47;
    --gold-deep: #b4842f;
    --gold-ink: #c08a35;
    --brand-dark: #4a3510;
    --card-white: #ffffff;
    --card-grey: #ececec;
    --text-dark: #3a3a3a;
    --divider: #555555;
  }
  * { box-sizing: border-box; margin: 0; padding: 0; }
  html, body {
    width: 1200px;
    height: 900px;
    overflow: hidden;
    background: var(--page-bg);
    font-family: "Lato", sans-serif;
  }
  .sheet {
    width: 1200px;
    height: 900px;
    display: flex;
    flex-direction: column;
    align-items: center;
    justify-content: center;
    gap: 44px;
  }
  .card {
    width: 700px;
    height: 400px;
    border-radius: 34px;
    position: relative;
    overflow: hidden;
  }
  .card--front {
    background: linear-gradient(110deg, var(--gold-light) 0%, var(--gold-mid) 55%, var(--gold-deep) 100%);
    display: flex;
    align-items: center;
    justify-content: center;
  }
  .card--front .brand-name {
    font-size: 34px;
    font-weight: 700;
    letter-spacing: 0.32em;
    color: var(--brand-dark);
    text-transform: uppercase;
    padding-left: 0.32em;
  }
  .card--back {
    background: linear-gradient(110deg, var(--card-grey) 0%, var(--card-white) 60%, var(--card-white) 100%);
  }
  .card--back .brand-name {
    position: absolute;
    left: 52px;
    top: 78px;
    font-size: 26px;
    font-weight: 400;
    letter-spacing: 0.3em;
    color: var(--gold-ink);
    text-transform: uppercase;
  }
  .contact-block {
    position: absolute;
    right: 46px;
    bottom: 58px;
    display: flex;
    align-items: stretch;
    gap: 18px;
  }
  .person {
    display: flex;
    flex-direction: column;
    justify-content: flex-end;
    text-align: right;
    padding-bottom: 2px;
  }
  .person__role {
    font-size: 17px;
    color: var(--text-dark);
  }
  .person__name {
    font-size: 21px;
    font-weight: 700;
    color: var(--gold-ink);
    text-transform: uppercase;
    letter-spacing: 0.02em;
  }
  .divider {
    width: 1.5px;
    background: var(--divider);
  }
  .contact-list {
    list-style: none;
    display: flex;
    flex-direction: column;
    gap: 9px;
  }
  .contact-list li {
    display: flex;
    align-items: center;
    gap: 10px;
    font-size: 17px;
    color: var(--text-dark);
  }
  .contact-list svg {
    width: 17px;
    height: 17px;
    flex: none;
    fill: var(--gold-ink);
  }
</style>
</head>
<body>
<main class="sheet">
  <section class="card card--front" aria-label="Card front">
    <span class="brand-name">Tornvel Skinheal</span>
  </section>

  <section class="card card--back" aria-label="Card back">
    <span class="brand-name">Tornvel Skinheal</span>

    <div class="contact-block">
      <div class="person">
        <span class="person__role">Director</span>
        <span class="person__name">Dana Whitfield</span>
      </div>
      <div class="divider"></div>
      <ul class="contact-list">
        <li>
          <svg viewBox="0 0 24 24" aria-hidden="true"><path d="M6.6 10.8a15.1 15.1 0 0 0 6.6 6.6l2.2-2.2a1 1 0 0 1 1-.25 11.4 11.4 0 0 0 3.6.57 1 1 0 0 1 1 1V20a1 1 0 0 1-1 1A17 17 0 0 1 3 4a1 1 0 0 1 1-1h3.5a1 1 0 0 1 1 1c0 1.25.2 2.45.57 3.57a1 1 0 0 1-.25 1z"/></svg>
          555-014-2210
        </li>
        <li>
          <svg viewBox="0 0 24 24" aria-hidden="true"><path d="M7 3h10v5H7zM4 9h16a2 2 0 0 1 2 2v6h-4v4H6v-4H2v-6a2 2 0 0 1 2-2zm4 6v4h8v-4z"/></svg>
          555-014-2211
        </li>
        <li>
          <svg viewBox="0 0 24 24" aria-hidden="true"><path d="M12 2a10 10 0 1 0 0 20 10 10 0 0 0 0-20zm6.9 6h-2.9a15.6 15.6 0 0 0-1.4-3.6A8 8 0 0 1 18.9 8zM12 4c.8 1.2 1.5 2.5 1.9 4h-3.8c.4-1.5 1.1-2.8 1.9-4zM4.3 14a8 8 0 0 1 0-4h3.4a16 16 0 0 0 0 4zm.8 2h2.9c.3 1.3.8 2.5 1.4 3.6A8 8 0 0 1 5.1 16zM8 8H5.1a8 8 0 0 1 4.3-3.6C8.8 5.5 8.3 6.7 8 8zm4 12c-.8-1.2-1.5-2.5-1.9-4h3.8c-.4 1.5-1.1 2.8-1.9 4zm2.3-6H9.7a14 14 0 0 1 0-4h4.6a14 14 0 0 1 0 4zm.3 5.6c.6-1.1 1.1-2.3 1.4-3.6h2.9a8 8 0 0 1-4.3 3.6zm1.7-5.6a16 16 0 0 0 0-4h3.4a8 8 0 0 1 0 4z"/></svg>
          www.tornvel-skinheal.com
        </li>
        <li>
          <svg viewBox="0 0 24 24" aria-hidden="true"><path d="M12 2a7 7 0 0 0-7 7c0 5.2 7 13 7 13s7-7.8 7-13a7 7 0 0 0-7-7zm0 9.5A2.5 2.5 0 1 1 12 6.5a2.5 2.5 0 0 1 0 5z"/></svg>
          4120 Maple Row Bldg. B, suite 118
        </li>
      </ul>
    </div>
  </section>
</main>
</body>
</html>
```